VitaNook Cookbook Cover

I need a design (front and back) for a cookbook cover. Our partners are looking for a few ideas to pick from.
You can see the style for one of the cookbooks we currently carry - uploaded with this brief.
This cookbook is a little different than most cookbooks out there. It is a cancer-fighting cookbook but we don't want it to be so cancer focused that people who don't have cancer will not buy. The book starts out with a section for Foods that Help, then goes to another section called Foods that Hurt. Then, we provide a Recipes section from the ingredients found in Foods that Help. Finally, the last section is called Beyond the Plate and deals with healthy lifestyle habits. You can see a rough draft of the content of the book at the link below. Please keep in mind that the current covers you see are not at all what we want. These were just put there to fill in the space.
Link for cookbook content: https://www.filecrate-example.net/s/4kq92mzx81pwtrd/The%20Bright%20Spoon%20-%20EDITED.pdf?dl=0
The title: The Bright Spoon
Subtitle: Fighting Cancer One Meal at a Time
Author: Mirel Tasvan
The company that puts the book out is VitaNook. It would be nice to have the logo somewhere small. Logo can be found here: https://www.filecrate-example.net/s/hzr37tqb05vnc2e/VitaNook%20Logo%20%26%20Guidelines.zip?dl=0
Like "Serve Them Sunnier Days" attached to this brief, we do NOT want something somber but more on the bright side. Just make it look nice and fresh. It would also be nice to somehow incorporate the concept of the cancer ribbon or a silhouette of it in a way that is not upfront but can still be acknowledge. No need for it to be pink and if that does not work, than it's better just to leave it out.
For the back cover, you can design it but simply leave room for us to fill in some text. No need for a spine design as it will be spiral bound.
The file must be designed and saved in PHOTOSHOP format.
According to the designer, the dimensions are:
207mm x 270mm + 5mm bleed
If you want to use the recipe pictures somehow in the cover, just snatch a picture from the content PDF and we can always replace it with the original larger file at a later time. Unfortunately, I don't have the pictures uploaded in filecrate.

```html
<!DOCTYPE html>
<html lang="en">
<head>
<meta charset="utf-8">
<title>The Bright Spoon – Cover Spread</title>
<link rel="stylesheet" href="https://fonts.googleapis.com/css2?family=Open+Sans:wght@400;600;700;800&display=swap">
<style>
  :root {
    --page-bg: #e9e7e4;
    --paper: #f4f3f0;
    --title-red: #e2231a;
    --title-green: #6f9e2c;
    --ink: #3a3a3a;
    --ink-soft: #5e5e5e;
    --spine: #f7f7f5;
    --tray: #e6e2da;
  }
  * { box-sizing: border-box; margin: 0; padding: 0; }
  html, body { width: 1200px; height: 818px; overflow: hidden; background: var(--page-bg); font-family: "Open Sans", Arial, sans-serif; }
  .spread {
    position: absolute; left: 20px; top: 39px;
    width: 1160px; height: 740px;
    display: flex;
    box-shadow: 0 6px 24px rgba(0,0,0,.18);
  }
  .cover { position: relative; width: 567px; height: 740px; background: var(--paper); overflow: hidden; }
  .spine {
    position: relative; width: 26px; height: 740px; background: var(--spine);
    border-left: 1px solid #dcdad6; border-right: 1px solid #dcdad6;
  }
  .spine-title, .spine-author, .spine-publisher {
    position: absolute; left: 50%; white-space: nowrap;
    transform: translateX(-50%) rotate(90deg);
    font-weight: 800; line-height: 1;
  }
  .spine-title { top: 80px; font-size: 15px; }
  .spine-title .word-red { color: var(--title-red); }
  .spine-title .word-green { color: var(--title-green); }
  .spine-author { top: 360px; font-size: 11px; color: var(--ink); }
  .spine-publisher { top: 540px; font-size: 10px; font-weight: 700; color: var(--ink); }

  /* Back cover */
  .back-blurb { position: absolute; left: 70px; top: 40px; width: 330px; }
  .back-title { font-weight: 800; line-height: .95; margin-bottom: 14px; }
  .back-title .small { display: block; font-size: 9px; color: var(--title-red); }
  .back-title .word-red { font-size: 20px; color: var(--title-red); }
  .back-title .word-green { display: block; padding-left: 44px; font-size: 15px; color: var(--title-green); }
  .back-blurb p { font-size: 10.5px; line-height: 1.45; color: var(--ink); text-align: center; margin-bottom: 12px; }
  .back-author { font-size: 13px; font-weight: 600; color: var(--ink); text-align: center; margin-top: 8px; }
  .back-wrap-photo {
    position: absolute; right: 0; top: 60px; width: 160px; height: 520px;
    background:
      radial-gradient(ellipse 60px 40px at 90px 400px, #4c5d9a 0%, rgba(76,93,154,0) 100%),
      radial-gradient(ellipse 50px 35px at 60px 340px, #c9a866 0%, rgba(201,168,102,0) 100%),
      linear-gradient(180deg, var(--tray) 0%, #ddd7cc 100%);
  }

  /* Front cover */
  .hero-photo {
    position: absolute; left: 0; top: 60px; width: 470px; height: 520px;
    background:
      radial-gradient(ellipse 110px 60px at 350px 330px, #e0392b 0%, #e0392b 45%, rgba(224,57,43,0) 100%),
      radial-gradient(ellipse 70px 110px at 190px 180px, #d25a48 0%, rgba(210,90,72,0) 100%),
      radial-gradient(ellipse 150px 190px at 170px 210px, #c9b18a 0%, #d8c8aa 55%, rgba(216,200,170,0) 100%),
      radial-gradient(ellipse 60px 40px at 300px 300px, #8a6a48 0%, rgba(138,106,72,0) 100%),
      linear-gradient(135deg, #ece9e3 0%, var(--tray) 50%, #dcd6cb 100%);
  }
  .front-title { position: absolute; right: 36px; top: 60px; text-align: right; font-weight: 800; line-height: .88; }
  .front-title .small { display: block; font-size: 24px; color: var(--title-red); text-align: left; padding-left: 60px; }
  .front-title .word-red { display: block; font-size: 80px; color: var(--title-red); letter-spacing: -1px; }
  .front-title .word-green { display: block; font-size: 62px; color: var(--title-green); }
  .subtitle { position: absolute; right: 36px; top: 262px; font-size: 13px; color: var(--ink-soft); letter-spacing: .3px; }
  .front-author { position: absolute; right: 36px; top: 545px; font-size: 18px; font-weight: 800; color: #2a2a2a; letter-spacing: .5px; }

  /* Photo strips */
  .photo-strip { position: absolute; left: 0; bottom: 0; width: 100%; height: 160px; display: flex; align-items: flex-end; }
  .photo-tile { flex: 1; height: 100%; }
  .photo-tile.short { height: 82%; }
</style>
</head>
<body>
  <main class="spread">
    <section class="cover back-cover">
      <div class="back-wrap-photo" role="img" aria-label="Photo of berries and walnuts on a white wooden tray, continuing from the front cover"></div>
      <div class="back-blurb">
        <h2 class="back-title"><span class="small">The</span><span class="word-red">Bright</span><span class="word-green">Spoon</span></h2>
        <p>Lorem ipsum dolor sit amet, consetetur sadipscing elitr, sed diam nonumy eirmod tempor invidunt ut labore et dolore magna aliquyam erat, sed diam voluptua. At vero eos et accusam et justo duo dolores et ea rebum. Stet clita kasd gubergren, no sea takimata sanctus est Lorem ipsum dolor sit amet.</p>
        <p>Duis autem vel eum iriure dolor in hendrerit in vulputate velit esse molestie consequat, vel illum dolore eu feugiat nulla facilisis at vero eros et accumsan et iusto odio dignissim qui blandit praesent luptatum zzril delenit augue duis dolore te feugait nulla facilisi.</p>
        <p>Ut wisi enim ad minim veniam, quis nostrud exerci tation ullamcorper suscipit lobortis nisl ut aliquip ex ea commodo consequat.</p>
        <div class="back-author">Mirel Tasvan</div>
      </div>
      <div class="photo-strip">
        <div class="photo-tile short" style="background:linear-gradient(135deg,#e9a25a,#c46b3a)" role="img" aria-label="Photo of halved peaches with granola"></div>
        <div class="photo-tile" style="background:linear-gradient(135deg,#f0a6c2,#d9577f)" role="img" aria-label="Photo of a pink berry smoothie"></div>
        <div class="photo-tile short" style="background:linear-gradient(135deg,#d9a35c,#c6332c)" role="img" aria-label="Photo of waffles with strawberries and blueberries"></div>
        <div class="photo-tile" style="background:linear-gradient(135deg,#ece7df,#b79a74)" role="img" aria-label="Photo of a bowl of cinnamon oatmeal"></div>
        <div class="photo-tile short" style="background:linear-gradient(135deg,#7fa04b,#c9473d)" role="img" aria-label="Photo of fresh vegetable wraps"></div>
        <div class="photo-tile" style="background:linear-gradient(135deg,#5c7f3a,#2f4e63)" role="img" aria-label="Photo of a green salad"></div>
      </div>
    </section>

    <aside class="spine">
      <div class="spine-title"><span class="word-red">Bright</span> <span class="word-green">Spoon</span></div>
      <div class="spine-author">Mirel TASVAN</div>
      <div class="spine-publisher">VitaNook</div>
    </aside>

    <section class="cover front-cover">
      <div class="hero-photo" role="img" aria-label="Photo of a glass jar of granola with strawberries, nuts and a spoon on a white wooden tray"></div>
      <h1 class="front-title"><span class="small">The</span><span class="word-red">Bright</span><span class="word-green">Spoon</span></h1>
      <div class="subtitle">Fighting Cancer One Meal at a Time</div>
      <div class="front-author">Mirel TASVAN</div>
      <div class="photo-strip">
        <div class="photo-tile short" style="background:linear-gradient(135deg,#c9473d,#5b3b2a)" role="img" aria-label="Photo of a veggie burger"></div>
        <div class="photo-tile" style="background:linear-gradient(135deg,#e2dcc8,#7c9a4a)" role="img" aria-label="Photo of a creamy spinach soup"></div>
        <div class="photo-tile short" style="background:linear-gradient(135deg,#e04a2b,#b8301f)" role="img" aria-label="Photo of tomato soup with herbs"></div>
        <div class="photo-tile" style="background:linear-gradient(135deg,#f1b24a,#d98a24)" role="img" aria-label="Photo of roasted sweet potato cubes"></div>
        <div class="photo-tile short" style="background:linear-gradient(135deg,#c9c17a,#6f7f3a)" role="img" aria-label="Photo of a quinoa salad"></div>
        <div class="photo-tile" style="background:linear-gradient(135deg,#8c4a7a,#5f8f3a)" role="img" aria-label="Photo of a colourful slaw salad"></div>
      </div>
    </section>
  </main>
</body>
</html>
```